MOSLEN Environmental needs an upgrade to its current business cards design

We need an upgrade to our current business cards design, where the MOSLEN acronym is included, as possible and not being overloaded.
MOSLEN Environmental is an Environmental Consultancy Firm based in Sydney.
We would like to see creative designs different from the standard type of business cards (for example, rounded edges, different to standard size of common business cards.

Target Market(s)

industrial companies (oil & gas, petrochemical, mining, insolvency, finance and manufacturing), developers, architect firms, law firms.

Industry/Entity Type

Business

Contact Information for Business Card

logos (brand and acronym), if they don't appear overloaded.
name
role
name of company (MOSLEN Environmental),
address (Level 3, Suite 3C, 47-49 Dorrigan Lane, Wexmoor, NSW, 2188) landline (02 7314 2986)
mobile (staff member)
email (staff member) and
website (www.moslengreen.example).
Include: Contaminated Land, Site Remediation, Groundwater Assessment, Health and Ecological Risk Assessments, Acid Sulfate Soils, Waste Classification.

Font styles to use
Serif
Sans Serif

Requirements
Must have
• A creative design different to the standard type of business cards.
Nice to have
• Rounded edges
• Different size of business cards rather than the standard size.
Should not have
• Preferable not to use white colour background, unless it is required from a creative design proposed.
• Not an overloaded design.
• Avoid black colours

```html
<!DOCTYPE html>
<html lang="en">
<head>
<meta charset="utf-8">
<title>MOSLEN Environmental – Business Card</title>
<link rel="stylesheet" href="https://fonts.googleapis.com/css2?family=Arimo:wght@700&display=swap">
<style>
  :root {
    --card-green: #009a4a;
    --ink-white: #ffffff;
  }
  html, body {
    margin: 0;
    padding: 0;
    width: 1200px;
    height: 686px;
    overflow: hidden;
    background: var(--card-green);
  }
  .card {
    position: relative;
    width: 1200px;
    height: 686px;
    background: var(--card-green);
    font-family: "Arimo", Arial, sans-serif;
    font-weight: 700;
    color: var(--ink-white);
  }
  .card__holes {
    position: absolute;
    inset: 0;
  }
  .acronym {
    margin: 0;
    padding: 0;
    list-style: none;
  }
  .acronym__row {
    position: absolute;
    left: 82px;
    display: flex;
    align-items: baseline;
    white-space: nowrap;
  }
  .acronym__initial {
    display: inline-block;
    width: 92px;
    text-align: center;
    font-size: 100px;
    line-height: 1;
  }
  .acronym__rest {
    margin-left: 8px;
    font-size: 42px;
    line-height: 1;
    letter-spacing: 0.2px;
  }
  .acronym__row--m { top: 75px; }
  .acronym__row--o { top: 165px; }
  .acronym__row--s { top: 255px; }
  .acronym__row--l { top: 345px; }
  .acronym__row--e { top: 435px; }
  .acronym__row--n { top: 525px; }
</style>
</head>
<body>
  <main class="card">
    <svg class="card__holes" width="1200" height="686" viewBox="0 0 1200 686" aria-hidden="true">
      <circle cx="51" cy="30" r="17" fill="#ffffff"/>
      <circle cx="1149" cy="30" r="17" fill="#ffffff"/>
      <circle cx="51" cy="657" r="17" fill="#ffffff"/>
      <circle cx="1149" cy="657" r="17" fill="#ffffff"/>
    </svg>

    <ul class="acronym" aria-label="MOSLEN">
      <li class="acronym__row acronym__row--m"><span class="acronym__initial">M</span><span class="acronym__rest">ONITORING</span></li>
      <li class="acronym__row acronym__row--o"><span class="acronym__initial">O</span><span class="acronym__rest">VERSIGHT (AND)</span></li>
      <li class="acronym__row acronym__row--s"><span class="acronym__initial">S</span><span class="acronym__rest">AMPLING (OF)</span></li>
      <li class="acronym__row acronym__row--l"><span class="acronym__initial">L</span><span class="acronym__rest">ANDS,</span></li>
      <li class="acronym__row acronym__row--e"><span class="acronym__initial">E</span><span class="acronym__rest">COSYSTEMS (AND)</span></li>
      <li class="acronym__row acronym__row--n"><span class="acronym__initial">N</span><span class="acronym__rest">ATURE</span></li>
    </ul>
  </main>
</body>
</html>
```